Bright Harbor Counseling Letterhead for hip modern business

I would like some ombre use of the colors in the logo hip letterhead that incorporates logo colors and feel, needs to connect with young professionals and college students. i need to be able to write letters to schools to excuse absences as well. i like color blocks on one side preferably using colors from the attached logo design.

Target Market(s)

high income young people, young adults and college students

Industry/Entity Type

mental health

Font styles to use
Serif
Sans Serif

Colors
0054AA
0677BA
7BADD7
CADEEF
E8F1F8
0094D4
00A9DD
6FCCEA
C7EBF8
E9F6FB
00AB8E
00BBA5
67D7C9
C6EFE9
E9F9F6
59FF00
82FF00
B8FF75
E3FFCB
F4FFEA
A7469A
B969AE
D3A5CF
EDDBEB
F8F0F9
6B429C
8869AF
B7A5CE
E3DAEB
F3F0F8

Requirements
Must have
• a modern hip feel, somewhat color

```html
<!DOCTYPE html>
<html lang="en">
<head>
<meta charset="utf-8">
<title>Bright Harbor Counseling – Stationery</title>
<link rel="stylesheet" href="https://fonts.googleapis.com/css2?family=Josefin+Sans:wght@300&family=Open+Sans:wght@400;600&family=Great+Vibes&display=swap">
<style>
  :root{
    --bg:#e6e6e6;
    --paper:#ffffff;
    --ink:#3a3a3a;
    --muted:#6a6a6a;
    --navy:#2f4f8f;
    --sky:#5aa0d0;
    --blue:#3f74b5;
    --orchid:#b06aa8;
    --violet:#8a5aa5;
    --teal:#6cc3bb;
    --line:#d9d9d9;
  }
  *{box-sizing:border-box;margin:0;padding:0}
  html,body{width:1200px;height:880px;overflow:hidden;background:var(--bg)}
  body{position:relative;font-family:"Open Sans",Arial,sans-serif;color:var(--ink)}
  .sheet{position:absolute;background:var(--paper);box-shadow:0 2px 8px rgba(0,0,0,.12);overflow:hidden}

  .band{position:absolute;left:0;right:0;bottom:0;display:flex}
  .band span:nth-child(1){background:var(--sky);flex:1.1}
  .band span:nth-child(2){background:var(--blue);flex:1.1}
  .band span:nth-child(3){background:var(--orchid);flex:1.1}
  .band span:nth-child(4){background:var(--violet);flex:1}
  .band span:nth-child(5){background:var(--teal);flex:1}

  .brand{display:flex;align-items:center;gap:8px;font-family:"Josefin Sans",Arial,sans-serif;font-weight:300;color:var(--ink);white-space:nowrap}
  .brand-dot{border-radius:50%;background:var(--violet);flex:none}

  /* Letterhead */
  .letterhead{left:40px;top:45px;width:600px;height:790px}
  .letterhead .brand{position:absolute;left:44px;top:70px;font-size:25px}
  .letterhead .brand-dot{width:22px;height:22px}
  .letterhead .accent{position:absolute;right:0;top:0;width:190px;height:140px;
    background:radial-gradient(circle at 35% 70%,#6fb6e0 0,#6fb6e0 25%,transparent 55%),
               radial-gradient(circle at 75% 35%,#a24d93 0,transparent 55%),
               linear-gradient(135deg,#9a6db0,#4f7fc4);opacity:.85;border-bottom-left-radius:70px}
  .letter{position:absolute;left:58px;top:150px;width:490px;font-size:10.5px;line-height:1.55}
  .letter .date{margin-bottom:10px}
  .letter .recipient{margin-bottom:22px}
  .letter .recipient strong{font-weight:600}
  .letter p{margin-bottom:14px;color:#444}
  .letter .signature{font-family:"Great Vibes",cursive;font-size:28px;color:var(--navy);margin-top:-6px}
  .contact-line{position:absolute;right:26px;bottom:26px;text-align:right;font-size:10.5px;color:var(--muted);line-height:1.6}
  .contact-line svg{vertical-align:-1px;margin-right:3px}
  .letterhead .band{height:16px}

  /* Envelopes */
  .env-front{left:690px;top:45px;width:470px;height:225px}
  .env-front .brand{position:absolute;left:24px;top:30px;font-size:15px}
  .env-front .brand-dot{width:13px;height:13px}
  .env-front .divider{position:absolute;left:262px;top:24px;width:1px;height:40px;background:var(--line)}
  .env-front .return-address{position:absolute;left:276px;top:27px;font-size:9px;color:var(--muted);line-height:1.5}
  .env-front .window{position:absolute;left:40px;top:96px;width:200px;height:60px;border:1px solid #e0e0e0;background:#f4f4f4;border-radius:2px}
  .env-front .band{height:11px}

  .env-back{left:690px;top:295px;width:470px;height:235px}
  .env-back svg.flap{position:absolute;left:0;top:0}
  .env-back .brand{position:absolute;left:50%;top:44px;transform:translateX(-50%);font-size:13px}
  .env-back .brand-dot{width:11px;height:11px}

  /* Business cards */
  .card{top:575px;width:225px;height:135px}
  .card-front{left:690px}
  .card-front .brand{position:absolute;left:12px;top:26px;font-size:8.5px;gap:5px}
  .card-front .brand-dot{width:8px;height:8px}
  .card-front .person{position:absolute;right:12px;top:14px;text-align:right}
  .card-front .person .name{font-size:10px;font-weight:600;color:var(--navy);line-height:1.3}
  .card-front .person .role{font-size:6.5px;color:var(--muted)}
  .card-front .rule{position:absolute;left:12px;right:12px;top:46px;height:1px;background:#8a8a8a}
  .card-front .details{position:absolute;left:12px;top:66px;font-size:7.5px;line-height:1.65;color:var(--muted);list-style:none}
  .card-front .details svg{vertical-align:-1px;margin-right:4px}
  .card .band{height:8px}
  .card-back{left:935px}
  .card-back .brand{position:absolute;left:50%;top:50%;transform:translate(-50%,-50%);font-size:15px}
  .card-back .brand-dot{width:13px;height:13px}
</style>
</head>
<body>

<section class="sheet letterhead">
  <div class="accent" role="img" aria-label="Soft colour blend in the brand blues and purples"></div>
  <div class="brand"><span class="brand-dot"></span>Bright Harbor Counseling</div>

  <div class="letter">
    <div class="date">February 21, 2021</div>
    <div class="recipient"><strong>Mr. Owen Carter,</strong><br>Marketing Head<br>Northfield College<br>27 Elm Quad,<br>Northfield XY 0318</div>
    <p>Dear Sir,</p>
    <p>Lorem ipsum dolor sit amet, consectetur adipiscing elit. Donec orci purus, luctus vitae dignissim eu, iaculis sed purus. Vivamus faucibus, ipsum nec aliquet viverra, leo mauris condimentum ligula, sit amet sagittis enim ligula quis arcu. Nam egestas tortor id nisi porttitor mattis. In tortor ante, ultricies in suscipit a, tempus non massa. Vivamus et auctor mi. Fusce vel massa nulla. Phasellus nec eros mauris, et scelerisque orci.</p>
    <p>Donec malesuada orci vitae nulla accumsan porta a id massa. Quisque accumsan iaculis magna sit amet fringilla. Maecenas consequat eget tincidunt semper, odio nibh rutrum mi, id feugiat ante nisi eu risus. Vestibulum nunc orci, rhoncus a placerat in, mi. Quisque scelerisque sagittis nulla at porttitor. Donec malesuada orci vitae nulla accumsan porta a id massa. Accumsan iaculis magna sit amet fringilla. Maecenas consequat, magna eget tincidunt semper, odio nibh rutrum mi, ante nisi eu risus. Vestibulum nunc orci, rhoncus a placerat in, ultricies in mi. Cras mattis varius eros, vel fringilla eget. Quisque scelerisque sagittis nulla at porttitor.</p>
    <p>Sed id augue vitae urna commodo aliquet a quam. Pellentesque arcu velit, cursus et malesuada ut, consequat et diam. Nullam rhoncus id ullamcorper vitae, rhoncus et arcu. In ultricies ultricies nulla, ut rutrum nisi iaculis at. Donec eu magna a pharetra faucibus. Fusce aliquet faucibus ultricies. Morbi semper, est id tincidunt gravida, sem arcu adipiscing lacus, ac blandit nulla leo eu purus. Quisque nec diam sed risus consectetur a cumsan quis nibh. Vestibulum id purus lorem.</p>
    <p>Thank you</p>
    <p style="margin-bottom:4px">Regards,</p>
    <div class="signature">Mara Ellison</div>
  </div>

  <div class="contact-line">
    482 Lantern Row, Ste 210, Harborview, XY 40118<br>
    <svg width="9" height="9" viewBox="0 0 10 10"><path d="M2 1l2 2-1 1.5c.7 1.4 1.6 2.3 3 3L7.5 6.5l2 2-1.3 1.3C4.5 9.5.5 5.5.2 2.3z" fill="var(--blue)"/></svg>555-014-3822 &nbsp;|&nbsp;
    <svg width="10" height="8" viewBox="0 0 10 8"><rect x=".5" y=".5" width="9" height="7" rx="1" fill="none" stroke="var(--blue)"/><path d="M.5 1l4.5 3.5L9.5 1" fill="none" stroke="var(--blue)"/></svg>hello@brightharborcounseling.com &nbsp;|&nbsp;
    <svg width="9" height="9" viewBox="0 0 10 10"><circle cx="5" cy="5" r="4.3" fill="none" stroke="var(--blue)"/><path d="M.7 5h8.6M5 .7c-2.4 2.6-2.4 6 0 8.6M5 .7c2.4 2.6 2.4 6 0 8.6" fill="none" stroke="var(--blue)" stroke-width=".8"/></svg>www.brightharborcounseling.com
  </div>
  <div class="band"><span></span><span></span><span></span><span></span><span></span></div>
</section>

<section class="sheet env-front">
  <div class="brand"><span class="brand-dot"></span>Bright Harbor Counseling</div>
  <div class="divider"></div>
  <div class="return-address">482 Lantern Row,<br>Ste 210, Harborview, XY 40118</div>
  <div class="window"></div>
  <div class="band"><span></span><span></span><span></span><span></span><span></span></div>
</section>

<section class="sheet env-back">
  <svg class="flap" width="470" height="235" viewBox="0 0 470 235">
    <path d="M0 6 L235 130 L470 6" fill="none" stroke="#e2e2e2" stroke-width="1.5"/>
    <path d="M0 235 L200 120 M470 235 L270 120" fill="none" stroke="#ececec" stroke-width="1"/>
  </svg>
  <div class="brand"><span class="brand-dot"></span>Bright Harbor Counseling</div>
</section>

<section class="sheet card card-front">
  <div class="brand"><span class="brand-dot"></span>Bright Harbor Counseling</div>
  <div class="person"><div class="name">Mara Ellison</div><div class="role">President &amp; CEO</div></div>
  <div class="rule"></div>
  <ul class="details">
    <li><svg width="7" height="7" viewBox="0 0 10 10"><path d="M2 1l2 2-1 1.5c.7 1.4 1.6 2.3 3 3L7.5 6.5l2 2-1.3 1.3C4.5 9.5.5 5.5.2 2.3z" fill="var(--navy)"/></svg>(555) 018 2264</li>
    <li><svg width="7" height="7" viewBox="0 0 10 10"><path d="M2 1l2 2-1 1.5c.7 1.4 1.6 2.3 3 3L7.5 6.5l2 2-1.3 1.3C4.5 9.5.5 5.5.2 2.3z" fill="var(--navy)"/></svg>(555) 017 9931</li>
    <li><svg width="8" height="6" viewBox="0 0 10 8"><rect x=".5" y=".5" width="9" height="7" rx="1" fill="none" stroke="var(--navy)"/><path d="M.5 1l4.5 3.5L9.5 1" fill="none" stroke="var(--navy)"/></svg>mara@brightharborcounseling.com</li>
    <li><svg width="7" height="7" viewBox="0 0 10 10"><circle cx="5" cy="5" r="4.3" fill="none" stroke="var(--navy)"/></svg>www.brightharborcounseling.com</li>
  </ul>
  <div class="band"><span></span><span></span><span></span><span></span><span></span></div>
</section>

<section class="sheet card card-back">
  <div class="brand"><span class="brand-dot"></span>Bright Harbor Counseling</div>
</section>

</body>
</html>
```